Construction Company Needs Letterhead Design

We recently had a new logo designed and would like to have our letterhead updated to a trendier design. We are a concrete construction company based out of Iowa, but do work for Agricultural businesses across the Midwest.

Industry/Entity Type

Construction

Colors
ec1f27
000000
ffffff

Requirements
Must have
• Must stay within our current color scheme of red/black/white. Must have have our address, phone number, e-mail address, etc. printed on the letterhead as well.

```html
<!DOCTYPE html>
<html lang="en">
<head>
<meta charset="utf-8">
<title>Brenner Farm Labor Services – Letterhead</title>
<link rel="stylesheet" href="https://fonts.googleapis.com/css2?family=Montserrat:wght@400;700&family=Lato:wght@400&display=swap">
<style>
  :root {
    --brand-red: #ec1f27;
    --brand-black: #000000;
    --paper: #ffffff;
    --band: #231f20;
    --ink: #3a3a3a;
    --backdrop: #e9e9e9;
  }
  * { box-sizing: border-box; margin: 0; padding: 0; }
  html, body { width: 1200px; height: 900px; overflow: hidden; }
  body {
    background: var(--backdrop);
    display: flex;
    align-items: center;
    justify-content: center;
    font-family: "Lato", sans-serif;
  }
  .letterhead {
    position: relative;
    width: 608px;
    height: 860px;
    background: var(--paper);
    box-shadow: 0 6px 24px rgba(0,0,0,0.12);
    overflow: hidden;
  }
  .letterhead__header {
    display: flex;
    justify-content: space-between;
    align-items: flex-start;
    padding: 62px 56px 0 56px;
  }
  .brand {
    display: flex;
    align-items: center;
    gap: 10px;
  }
  .brand__square {
    width: 26px;
    height: 26px;
    background: var(--brand-red);
  }
  .brand__name {
    font-family: "Montserrat", sans-serif;
    font-weight: 700;
    font-size: 15px;
    letter-spacing: 0.5px;
    text-transform: uppercase;
    color: var(--brand-black);
    line-height: 1.15;
  }
  .sender-address {
    font-size: 9.5px;
    line-height: 1.4;
    color: var(--ink);
    text-align: left;
  }
  .letter-body {
    padding: 70px 56px 0 140px;
    font-size: 10px;
    line-height: 1.45;
    color: var(--ink);
  }
  .letter-body p { margin-bottom: 14px; text-align: left; }
  .signoff { margin-top: 14px; }
  .signature {
    width: 120px;
    height: 34px;
    background: linear-gradient(90deg, rgba(40,110,200,0.18), rgba(40,110,200,0.05));
    border-radius: 4px;
  }
  .signoff__role {
    font-size: 10px;
    color: var(--ink);
    margin-top: 2px;
  }
  .footer-rule {
    position: absolute;
    left: 150px;
    right: 0;
    bottom: 52px;
    height: 4px;
    background: var(--brand-red);
  }
  .contact-band {
    position: absolute;
    left: 0;
    right: 0;
    bottom: 0;
    height: 44px;
    background: var(--band);
    display: flex;
    align-items: center;
    justify-content: flex-end;
    gap: 12px;
    padding-right: 30px;
    font-size: 9.5px;
    color: var(--paper);
  }
  .contact-band__label { color: var(--brand-red); margin-right: 3px; }
</style>
</head>
<body>
  <article class="letterhead">
    <header class="letterhead__header">
      <div class="brand">
        <span class="brand__square"></span>
        <span class="brand__name">Brenner<br>Farm Labor Services</span>
      </div>
      <address class="sender-address" style="font-style: normal;">
        4120 Prairie Road<br>Ames, Iowa 50010
      </address>
    </header>

    <section class="letter-body">
      <p>Letterhead samples are a great way of deciding what kind of letterhead you want to design for you and your company. The internet has a ton of great letterhead samples to browse through. Whether you want something simple, with just a couple lines of text of your business information, or something decorative and stunning, with photos and logos on the top and bottom of the page, it will be easy to find what you want, because there are samples online for basically any type of letterhead you could want.</p>
      <p>Any business could easily benefit from browsing through some letterhead samples, if only to get an idea for what kind of letterhead their company might want. Letterheads are just one of the tools that a business professional could use to help increase their customer base, and to really be memorable to everyone they write a letter to. Letterhead is quite an effective tool for marketing and advertising, but because it's such a simple and well known idea, it is often unfairly overlooked. Make sure you don't make that mistake, and make some letterhead samples of your own today.</p>
      <p>Whether you want to get new customers to remember you and become part of your clientele, or you just want to send out friendly reminders to your existing clients, customizing your own letterhead samples can really help you out. Try out some letterhead samples and you will not regret it, and I'm sure you will add a new tool to your business' arsenal of networking, marketing, and advertising tools.</p>
      <div class="signoff">
        <div class="signature" role="img" aria-label="Handwritten signature of Martin Hale"></div>
        <div class="signoff__role">company director</div>
      </div>
    </section>

    <div class="footer-rule"></div>
    <footer class="contact-band">
      <span><span class="contact-band__label">p:</span>(555) 410 2280</span>
      <span><span class="contact-band__label">f:</span>(555) 410 2281</span>
      <span><span class="contact-band__label">e:</span>info@brennercrete.com</span>
      <span><span class="contact-band__label">w:</span>www.brennercrete.com</span>
    </footer>
  </article>
</body>
</html>
```